Electronics Store Business Rebranding and Refresh

We have previously been a stockist of an Electronics company, and now are going completely independent!
We have a basic branding which we like, and would like to continue this, as well as "flash-up" our Veltrano branding for our own brand products.
We would like the Veltrano branding come through as a high quality brand. It incorporates a wide range of products such as computer accessories, audio/visual cables, mobile cables, and other electronics.
We are thinking the red and blue colour scheme of the Veltrano brand works well and would like to keep them.
So, what do we need???
1)
Our current Corby Lane logo, has a yellow back, we would like a copy of this with a white background, and a copy with a transparent background. I have attached the "Corby Lane Electrical and security" logo in hi-res. We would like this changed to "Corby Lane electronics direct" as per the low res sample i have attached.
2)
Our Veltrano logo needs Flashing up, this needs to look like a quality brand. We would like a copy of this with a white background and a copy with a transparent background.
3)
Signage:
sign 1. 2400mm long x 280mm high. This is for a lightbox hanging from the verandah. I am thinking Corby Lane on the left half, Veltrano on the right half, and the website along the bottom. Leave a 20mm margin to allow for the perspex to fit into the track.
sign 2. 880mm wide x 2330mm high. This is a window decal. we would like to install this on the inside of the window, but visible from the outside (so it can't be grafitied). We would like to have several big pictures of items we sell, such as R/C helicopters, R/c cars, Zorvo batteries, plug packs, solar panels, hdmi cables, rca cables, rj45 cables, tv cables etc.
sign 3. front left windows (next to each other) the first is 1280mm wide x 840mm high, the second is 1330mm wide x 840mm high. I am not sure what to put on these windows. They are just above head height outside. Maybe a combination of things from the other signs etc???
sign 4. possibly same as sign 2, but 550mm wide x 2430 high.
4)
Header cards. We want these to 60mm wide x 60mm high (when folded). Similar to the sample attached, but blue and yellow instead of blue and red. we do not need the blank white panel on the back. We would like the Veltrano logo on this. as well as space for a dymo label that we print instore. (the label is 54mm wide x 24mm high)
5)
label for packaging 75mm wide x 50mm high (approx)
we want a generic label that can go on the front of our clamshell boxes. This must have the Veltrano logo on it.
We want to be able to run this through a laser printer (possibly on A4)
so we can print the product description on the bottom half of the label. The other posibility for this is if we go with a dymo compatible label of similar size.???
6)
Business Card design. We are thinking similar to our old business card design, just with our current Corby Lane logo, and contact details.
maybe fit the Veltrano logo in somewhere to tie the two brands together.
Details:
Corby Lane Electronics Direct
2273 Tarawick Street
Rotorua
Ph (07) 5926170
www.corbylane-example.co.nz
email shop@corbylane-example.co.nz

This looks like a lot of work, but i think it should be fairly straight forward once the Veltrano logo is designed.
I have added some sample pics to hopefully give some ideas.
maybe sign 3, could have pictures in a square icon style???
get creative.

```html
<!DOCTYPE html>
<html lang="en">
<head>
<meta charset="utf-8">
<title>Visiting Card – Corby Lane Electronics Direct</title>
<link rel="stylesheet" href="https://fonts.googleapis.com/css2?family=Arimo:ital,wght@0,400;0,700;1,400&family=Libre+Baskerville:wght@700&display=swap">
<style>
  :root {
    --board-light: #f4f4f4;
    --board-mid: #d9d9d9;
    --board-dark: #bdbdbd;
    --ink: #1b1b1b;
    --ink-soft: #333333;
    --brand-ink: #1c1c1c;
    --badge: #c8c6e4;
    --badge-edge: #6f6c99;
    --sub-red: #c9252c;
    --yellow: #ffd21a;
    --yellow-deep: #f6c400;
    --grey-band: #d6d6d6;
    --navy: #23205a;
    --white: #ffffff;
  }
  * { box-sizing: border-box; margin: 0; padding: 0; }
  html, body { width: 1200px; height: 1000px; overflow: hidden; }
  body {
    position: relative;
    font-family: "Arimo", Arial, sans-serif;
    color: var(--ink);
    background:
      linear-gradient(125deg, transparent 30%, rgba(255,255,255,.55) 42%, transparent 54%),
      linear-gradient(140deg, transparent 55%, rgba(255,255,255,.45) 66%, transparent 76%),
      linear-gradient(180deg, var(--board-light), var(--board-mid) 60%, var(--board-dark));
  }

  .sheet-title {
    position: absolute; left: 820px; top: 44px;
    font-family: "Libre Baskerville", Georgia, serif;
    font-weight: 700; font-size: 38px; letter-spacing: 1px; color: #1e1e1e;
  }
  .sheet-size {
    position: absolute; left: 820px; top: 93px;
    font-size: 15px; color: #1e1e1e;
  }

  .card {
    position: absolute; width: 386px; height: 228px;
    background: var(--white); overflow: hidden;
    box-shadow: 3px 4px 7px rgba(0,0,0,.45);
  }
  .card--a { left: 152px; top: 170px; }
  .card--b { left: 645px; top: 170px; }
  .card--c { left: 152px; top: 446px; }
  .card--d { left: 645px; top: 446px; }
  .card--e { left: 152px; top: 725px; }
  .card--f { left: 645px; top: 725px; }

  /* store name lockup */
  .brand { position: absolute; display: flex; align-items: center; gap: 8px; }
  .brand__name {
    font-weight: 700; color: var(--brand-ink); line-height: 1.05;
    font-size: 20px; text-align: right;
  }
  .brand__badge {
    border-radius: 50%; background: var(--badge);
    border: 2px solid var(--badge-edge);
    width: 56px; height: 56px; flex: none;
  }
  .brand--lg .brand__name { font-size: 24px; }
  .brand--lg .brand__badge { width: 64px; height: 64px; }
  .brand--sm .brand__name { font-size: 16px; }
  .brand--sm .brand__badge { width: 46px; height: 46px; }

  /* house brand */
  .house {
    position: absolute; text-align: center; line-height: 1;
  }
  .house__name { font-weight: 700; color: var(--sub-red); font-size: 22px; letter-spacing: .5px; }
  .house__tag { font-size: 6.5px; letter-spacing: 1.6px; color: var(--ink-soft); margin-top: 3px; }
  .house--lg .house__name { font-size: 32px; }
  .house--lg .house__tag { font-size: 8px; letter-spacing: 2.4px; }
  .house--vertical { writing-mode: vertical-rl; }

  .contact { position: absolute; line-height: 1.25; }
  .contact__name { font-weight: 700; font-size: 13px; }
  .contact__role { font-size: 11px; }
  .contact__role--inline { font-style: italic; font-size: 9px; font-weight: 400; }
  .contact__line { font-size: 9px; }
  .contact__line b { font-weight: 700; }
  .contact--center { left: 0; right: 0; text-align: center; }
  .contact--right { right: 14px; text-align: right; }

  .band { position: absolute; left: 0; right: 0; }
  .band--grey { background: var(--grey-band); }
  .band--yellow {
    background:
      linear-gradient(115deg, transparent 58%, rgba(255,255,255,.55) 68%, transparent 78%, rgba(255,255,255,.4) 88%, transparent 96%),
      var(--yellow);
  }
  .band--yellow-flat { background: var(--yellow); }
  .band--navy {
    background:
      linear-gradient(115deg, transparent 62%, rgba(190,160,120,.6) 72%, transparent 80%, rgba(200,180,140,.5) 90%, transparent 97%),
      var(--navy);
    color: var(--white);
  }
  .band__site {
    position: absolute; left: 0; right: 0; text-align: center;
    font-weight: 700; font-size: 15px;
  }
  .band__services {
    position: absolute; left: 0; right: 0; text-align: center;
    font-size: 7.8px; white-space: nowrap;
  }
</style>
</head>
<body>

<h1 class="sheet-title">Visiting Card</h1>
<p class="sheet-size">Size : 85.6mm x 50.8mm&nbsp; (3.5 in x 2.0 in)</p>

<!-- Card A: grey name band -->
<section class="card card--a">
  <div class="brand" style="left:82px; top:12px;">
    <div class="brand__name">Corby Lane<br>Electronics Direct</div>
    <div class="brand__badge" role="img" aria-label="Store mascot badge"></div>
  </div>
  <div class="house" style="left:0; right:0; top:87px;">
    <div class="house__name">Veltrano</div>
    <div class="house__tag">HANDPICKED ELECTRONICS</div>
  </div>
  <div class="band band--grey" style="top:125px; height:55px;"></div>
  <div class="contact contact--center" style="top:131px;">
    <div class="contact__name">Reuben Hale - <span class="contact__role--inline">Managing Director</span></div>
    <div class="contact__line" style="margin-top:5px;">2273 Tarawick Street. Rotorua</div>
    <div class="contact__line"><b>P.</b> (07) 5926170 &nbsp;<b>E.</b> shop@corbylane-example.co.nz</div>
  </div>
  <div class="band band--yellow-flat" style="top:180px; height:48px;">
    <div class="band__site" style="top:7px;">www.corbylane-example.co.nz</div>
    <div class="band__services" style="top:30px;">Electrical Wiring | Alarm Systems | Home Ventilation | TV Aerials | Free-to-Air | Heatpumps</div>
  </div>
</section>

<!-- Card B: yellow top, navy base -->
<section class="card card--b">
  <div class="band band--yellow-flat" style="top:0; height:80px;"></div>
  <div class="brand" style="left:82px; top:12px;">
    <div class="brand__name">Corby Lane<br>Electronics Direct</div>
    <div class="brand__badge" role="img" aria-label="Store mascot badge"></div>
  </div>
  <div class="house" style="left:0; right:0; top:90px;">
    <div class="house__name">Veltrano</div>
    <div class="house__tag">HANDPICKED ELECTRONICS</div>
  </div>
  <div class="contact contact--center" style="top:137px;">
    <div class="contact__name">Reuben Hale - <span class="contact__role--inline">Managing Director</span></div>
    <div class="contact__line" style="margin-top:5px;">2273 Tarawick Street. Rotorua</div>
    <div class="contact__line"><b>P.</b> (07) 5926170 &nbsp;<b>E.</b> shop@corbylane-example.co.nz</div>
  </div>
  <div class="band band--navy" style="top:184px; height:44px;">
    <div class="band__site" style="top:5px;">www.corbylane-example.co.nz</div>
    <div class="band__services" style="top:27px;">Electrical Wiring | Alarm Systems | Home Ventilation | TV Aerials | Free-to-Air | Heatpumps</div>
  </div>
</section>

<!-- Card C: house brand left, details right -->
<section class="card card--c">
  <div class="brand brand--lg" style="left:14px; top:12px;">
    <div class="brand__name" style="text-align:left;">Corby Lane<br>Electronics Direct</div>
    <div class="brand__badge" role="img" aria-label="Store mascot badge"></div>
  </div>
  <div class="house house--lg" style="left:14px; top:118px; text-align:left;">
    <div class="house__name">Veltrano</div>
    <div class="house__tag">HANDPICKED ELECTRONICS</div>
  </div>
  <div class="contact contact--right" style="top:101px;">
    <div class="contact__name">Reuben Hale</div>
    <div class="contact__role">Managing Director</div>
    <div class="contact__line" style="margin-top:8px;">2273 Tarawick Street. Rotorua</div>
    <div class="contact__line"><b>P.</b> (07) 5926170</div>
    <div class="contact__line"><b>E.</b> shop@corbylane-example.co.nz</div>
  </div>
  <div class="band band--yellow" style="top:178px; height:50px;">
    <div class="band__site" style="top:8px;">www.corbylane-example.co.nz</div>
    <div class="band__services" style="top:31px;">Electrical Wiring | Alarm Systems | Home Ventilation | TV Aerials | Free-to-Air | Heatpumps</div>
  </div>
</section>

<!-- Card D: vertical house brand -->
<section class="card card--d">
  <div class="brand" style="left:14px; top:16px;">
    <div class="brand__name" style="text-align:left;">Corby Lane<br>Electronics Direct</div>
    <div class="brand__badge" role="img" aria-label="Store mascot badge"></div>
  </div>
  <div class="house house--lg house--vertical" style="right:10px; top:14px; height:160px;">
    <div class="house__name">Veltrano</div>
    <div class="house__tag" style="margin-top:0; margin-right:3px;">HANDPICKED ELECTRONICS</div>
  </div>
  <div class="contact" style="left:40px; width:300px; text-align:center; top:98px;">
    <div class="contact__name">Reuben Hale</div>
    <div class="contact__role">Managing Director</div>
    <div class="contact__line" style="margin-top:8px;">2273 Tarawick Street. Rotorua</div>
    <div class="contact__line"><b>P.</b> (07) 5926170</div>
    <div class="contact__line"><b>E.</b> shop@corbylane-example.co.nz</div>
  </div>
  <div class="band band--yellow" style="top:178px; height:50px;">
    <div class="band__site" style="top:8px;">www.corbylane-example.co.nz</div>
    <div class="band__services" style="top:31px;">Electrical Wiring | Alarm Systems | Home Ventilation | TV Aerials | Free-to-Air | Heatpumps</div>
  </div>
</section>

<!-- Card E: both marks side by side -->
<section class="card card--e">
  <div class="brand brand--sm" style="left:12px; top:18px;">
    <div class="brand__name" style="text-align:left;">Corby Lane<br>Electronics Direct</div>
    <div class="brand__badge" role="img" aria-label="Store mascot badge"></div>
  </div>
  <div class="house" style="left:238px; top:24px;">
    <div class="house__name" style="font-size:24px;">Veltrano</div>
    <div class="house__tag">HANDPICKED ELECTRONICS</div>
  </div>
  <div class="contact contact--center" style="top:95px;">
    <div class="contact__name">Reuben Hale</div>
    <div class="contact__role">Managing Director</div>
    <div class="contact__line" style="margin-top:10px;">2273 Tarawick Street. Rotorua</div>
    <div class="contact__line"><b>P.</b> (07) 5926170</div>
    <div class="contact__line"><b>E.</b> shop@corbylane-example.co.nz</div>
  </div>
  <div class="band band--yellow" style="top:180px; height:48px;">
    <div class="band__site" style="top:7px;">www.corbylane-example.co.nz</div>
    <div class="band__services" style="top:30px;">Electrical Wiring | Alarm Systems | Home Ventilation | TV Aerials | Free-to-Air | Heatpumps</div>
  </div>
</section>

<!-- Card F: vertical contact column -->
<section class="card card--f">
  <div class="contact" style="left:10px; top:14px; height:160px; writing-mode:vertical-rl; transform:rotate(180deg); text-align:right;">
    <div class="contact__line">2273 Tarawick Street. Rotorua</div>
    <div class="contact__line"><b>P.</b> (07) 5926170</div>
    <div class="contact__line"><b>E.</b> shop@corbylane-example.co.nz</div>
  </div>
  <div class="brand" style="left:92px; top:18px;">
    <div class="brand__name">Corby Lane<br>Electronics Direct</div>
    <div class="brand__badge" role="img" aria-label="Store mascot badge"></div>
  </div>
  <div class="house" style="left:60px; right:0; top:92px;">
    <div class="house__name">Veltrano</div>
    <div class="house__tag">HANDPICKED ELECTRONICS</div>
  </div>
  <div class="contact" style="left:60px; right:0; text-align:center; top:146px;">
    <div class="contact__name">Reuben Hale</div>
    <div class="contact__role">Managing Director</div>
  </div>
  <div class="band band--yellow" style="top:180px; height:48px;">
    <div class="band__site" style="top:7px;">www.corbylane-example.co.nz</div>
    <div class="band__services" style="top:30px;">Electrical Wiring | Alarm Systems | Home Ventilation | TV Aerials | Free-to-Air | Heatpumps</div>
  </div>
</section>

</body>
</html>
```